Background graphic for Vortapex profile

I need a graphic for the background image that appears on Vortapex behind my photo.
I am looking for an image that complements my About Me statement, "Directing patient-first marketing from strategy to execution to help healthcare companies reach the right people at just the right time." I am thinking something with a clock and people and connections. A single example is below and I am open to creative ideas.
1128 (w) x 191 (h) pixels, PNG or JPEG files and have a maximum size of 3MB

```html
<!DOCTYPE html>
<html lang="en">
<head>
<meta charset="utf-8">
<title>Vortapex Profile Background</title>
<link href="https://fonts.googleapis.com/css2?family=Inter:wght@400&display=swap" rel="stylesheet">
<style>
  :root {
    --navy-deep: #02024a;
    --navy: #060a6e;
    --blue-mid: #0a3f8f;
    --glow: #1a7fd0;
    --node-fill: #0b2f86;
    --line: #dfeaff;
    --frame: #3a4fc4;
    --white: #ffffff;
  }
  html, body {
    margin: 0;
    padding: 0;
    width: 1200px;
    height: 300px;
    overflow: hidden;
    background: var(--navy-deep);
    font-family: "Inter", sans-serif;
  }
  .banner {
    position: relative;
    width: 1200px;
    height: 300px;
    background: linear-gradient(90deg, var(--navy) 0%, var(--navy-deep) 30%, var(--blue-mid) 50%, var(--navy-deep) 75%, #01012a 100%);
  }
  .banner-glow {
    position: absolute;
    inset: 0;
    background: radial-gradient(ellipse 320px 200px at 623px 130px, rgba(40,150,230,0.55), rgba(10,60,150,0.2) 55%, transparent 80%);
  }
  .banner-art { position: absolute; inset: 0; }
  .frame { fill: none; stroke: var(--frame); stroke-width: 1.2; opacity: 0.7; }
  .link { stroke: var(--line); stroke-width: 1.2; opacity: 0.9; }
  .node { fill: var(--node-fill); stroke: var(--white); stroke-width: 2.5; }
  .node-small { fill: var(--node-fill); stroke: var(--white); stroke-width: 2; }
  .glyph { fill: var(--white); }
  .glyph-line { fill: none; stroke: var(--white); stroke-width: 1.8; stroke-linecap: round; stroke-linejoin: round; }
</style>
</head>
<body>
<div class="banner">
  <div class="banner-glow"></div>
  <svg class="banner-art" width="1200" height="300" viewBox="0 0 1200 300" xmlns="http://www.w3.org/2000/svg">
    <defs>
      <g id="user-glyph">
        <circle cx="0" cy="-2.5" r="2.6" class="glyph"/>
        <path d="M-5 5 Q-5 0.5 0 0.5 Q5 0.5 5 5 Z" class="glyph"/>
      </g>
    </defs>

    <!-- side frames -->
    <g class="side-frames">
      <path class="frame" d="M34 106 L86 122 L86 176 L34 192"/>
      <path class="frame" d="M73 74 L165 104 L165 194 L73 224"/>
      <path class="frame" d="M112 42 L245 82 L245 216 L112 256"/>
      <path class="frame" d="M152 10 L326 64 L326 236 L152 290"/>
      <line class="frame" x1="192" y1="0" x2="192" y2="300"/>
      <line class="frame" x1="231" y1="0" x2="231" y2="300"/>
      <path class="frame" d="M1166 106 L1114 122 L1114 176 L1166 192"/>
      <path class="frame" d="M1127 74 L1035 104 L1035 194 L1127 224"/>
      <path class="frame" d="M1088 42 L955 82 L955 216 L1088 256"/>
      <path class="frame" d="M1048 10 L874 64 L874 236 L1048 290"/>
      <line class="frame" x1="968" y1="0" x2="968" y2="300"/>
      <line class="frame" x1="1008" y1="0" x2="1008" y2="300"/>
    </g>

    <!-- connections -->
    <g class="links">
      <line class="link" x1="409" y1="129" x2="394" y2="70"/>
      <line class="link" x1="409" y1="129" x2="378" y2="175"/>
      <line class="link" x1="409" y1="129" x2="554" y2="91"/>
      <line class="link" x1="409" y1="129" x2="514" y2="172"/>
      <line class="link" x1="409" y1="129" x2="430" y2="216"/>
      <line class="link" x1="554" y1="91" x2="532" y2="61"/>
      <line class="link" x1="554" y1="91" x2="514" y2="172"/>
      <line class="link" x1="554" y1="91" x2="623" y2="147"/>
      <line class="link" x1="514" y1="172" x2="430" y2="216"/>
      <line class="link" x1="514" y1="172" x2="542" y2="225"/>
      <line class="link" x1="514" y1="172" x2="483" y2="273"/>
      <line class="link" x1="514" y1="172" x2="623" y2="147"/>
      <line class="link" x1="623" y1="147" x2="640" y2="81"/>
      <line class="link" x1="623" y1="147" x2="707" y2="108"/>
      <line class="link" x1="623" y1="147" x2="598" y2="204"/>
      <line class="link" x1="623" y1="147" x2="687" y2="214"/>
      <line class="link" x1="623" y1="147" x2="747" y2="180"/>
      <line class="link" x1="623" y1="147" x2="827" y2="129"/>
      <line class="link" x1="747" y1="180" x2="827" y2="129"/>
      <line class="link" x1="747" y1="180" x2="798" y2="236"/>
      <line class="link" x1="827" y1="129" x2="891" y2="95"/>
      <line class="link" x1="827" y1="129" x2="923" y2="145"/>
      <line class="link" x1="827" y1="129" x2="871" y2="176"/>
    </g>

    <!-- medical symbol node -->
    <g class="node-medical">
      <circle class="node" cx="409" cy="129" r="32"/>
      <circle cx="409" cy="129" r="20" fill="#3f63b8" role="img" aria-label="Medical staff symbol"/>
    </g>

    <!-- first aid node -->
    <g class="node-first-aid">
      <circle class="node" cx="554" cy="91" r="20"/>
      <rect x="545" y="84" width="18" height="15" rx="2" class="glyph"/>
      <rect x="550" y="80" width="8" height="5" rx="1" class="glyph-line"/>
      <rect x="552.5" y="87" width="3" height="9" fill="var(--node-fill)"/>
      <rect x="549.5" y="90" width="9" height="3" fill="var(--node-fill)"/>
    </g>

    <!-- single person node -->
    <g class="node-person">
      <circle class="node" cx="514" cy="172" r="32"/>
      <circle cx="514" cy="163" r="6" class="glyph"/>
      <path d="M504 183 Q504 171 514 171 Q524 171 524 183 Z" class="glyph"/>
    </g>

    <!-- central community node -->
    <g class="node-community">
      <circle class="node" cx="623" cy="147" r="38" stroke-width="3"/>
      <circle cx="610" cy="134" r="6" class="glyph"/>
      <circle cx="636" cy="134" r="6" class="glyph"/>
      <path d="M598 157 Q598 143 610 143 Q622 143 622 157 Z" class="glyph"/>
      <path d="M624 157 Q624 143 636 143 Q648 143 648 157 Z" class="glyph"/>
      <circle cx="623" cy="140" r="8" class="glyph" stroke="var(--node-fill)" stroke-width="2"/>
      <path d="M607 168 Q607 150 623 150 Q639 150 639 168 Z" class="glyph" stroke="var(--node-fill)" stroke-width="2"/>
    </g>

    <!-- small group node -->
    <g class="node-group">
      <circle class="node" cx="430" cy="216" r="20"/>
      <circle cx="424" cy="209" r="3.5" class="glyph"/>
      <circle cx="436" cy="209" r="3.5" class="glyph"/>
      <circle cx="430" cy="212" r="4" class="glyph" stroke="var(--node-fill)" stroke-width="1.2"/>
      <path d="M420 225 Q420 216 430 216 Q440 216 440 225 Z" class="glyph" stroke="var(--node-fill)" stroke-width="1.2"/>
    </g>

    <!-- phone node -->
    <g class="node-phone">
      <circle class="node-small" cx="640" cy="81" r="13"/>
      <rect x="635" y="73" width="10" height="16" rx="1.5" class="glyph-line" stroke-width="1.4"/>
      <path d="M636.5 82 L638.5 82 L639.5 79 L641 85 L642 82 L643.5 82" class="glyph-line" stroke-width="1"/>
    </g>

    <!-- heart node -->
    <g class="node-heart">
      <circle class="node-small" cx="707" cy="108" r="11"/>
      <path d="M707 113 L702 108 Q700 104 703.5 103 Q706 103 707 105.5 Q708 103 710.5 103 Q714 104 712 108 Z" class="glyph"/>
    </g>

    <!-- pill node -->
    <g class="node-pill">
      <circle class="node-small" cx="598" cy="204" r="13"/>
      <rect x="594" y="196" width="8" height="16" rx="4" class="glyph-line" stroke-width="1.5" transform="rotate(40 598 204)"/>
      <rect x="594" y="204" width="8" height="8" rx="3" class="glyph" transform="rotate(40 598 204)"/>
    </g>

    <!-- clock node -->
    <g class="node-clock">
      <circle class="node-small" cx="687" cy="214" r="15"/>
      <circle cx="687" cy="214" r="9" class="glyph-line"/>
      <path d="M687 209 L687 214 L691 216" class="glyph-line"/>
    </g>

    <!-- monitor node -->
    <g class="node-monitor">
      <circle class="node" cx="747" cy="180" r="26"/>
      <rect x="734" y="168" width="26" height="19" class="glyph-line"/>
      <path d="M730 190 L764 190" class="glyph-line" stroke-width="2.5"/>
      <path d="M736 179 L741 179 L743 172 L746 184 L749 174 L751 179 L758 179" class="glyph-line" stroke-width="1.4"/>
    </g>

    <!-- home node -->
    <g class="node-home">
      <circle class="node" cx="798" cy="236" r="20"/>
      <path d="M787 236 L798 227 L809 236" class="glyph-line" stroke-width="2.2"/>
      <path d="M790 234 L790 245 L806 245 L806 234 L798 228 Z" class="glyph"/>
      <rect x="795" y="238" width="5" height="7" fill="var(--node-fill)"/>
    </g>

    <!-- genetics node -->
    <g class="node-genetics">
      <circle class="node" cx="827" cy="129" r="32"/>
      <circle cx="827" cy="129" r="20" fill="#3f63b8" role="img" aria-label="DNA helix illustration"/>
    </g>

    <!-- small user nodes -->
    <g class="user-nodes">
      <circle class="node-small" cx="394" cy="70" r="10"/><use href="#user-glyph" x="394" y="70"/>
      <circle class="node-small" cx="532" cy="61" r="10"/><use href="#user-glyph" x="532" y="61"/>
      <circle class="node-small" cx="378" cy="175" r="10"/><use href="#user-glyph" x="378" y="175"/>
      <circle class="node-small" cx="542" cy="225" r="12"/><use href="#user-glyph" x="542" y="225"/>
      <circle class="node-small" cx="483" cy="273" r="10"/><use href="#user-glyph" x="483" y="273"/>
      <circle class="node-small" cx="891" cy="95" r="11"/><use href="#user-glyph" x="891" y="95"/>
      <circle class="node-small" cx="923" cy="145" r="14"/><use href="#user-glyph" x="923" y="145"/>
      <circle class="node-small" cx="871" cy="176" r="12"/><use href="#user-glyph" x="871" y="176"/>
    </g>
  </svg>
</div>
</body>
</html>
```